Healer at the Hearth needs business card

We need a business card that reflects the look and feel of the new website at www.healerathearth.ca

Target Market(s)

Our patient navigation and advocacy services are most commonly used by seniors who feel overwhelmed by the health care system and want someone on their side to advocate for their care. Individuals with ill parents or other family members may also come to rely on Healer at the Hearth to help them support their loved one through their health care journey. Ultimately, anyone who finds their health care experience challenging and wants someone completely focused on their needs can benefit from the services of our doctor / nurse team.

Industry/Entity Type

Business

Requirements
Must have
• One design tailored for two clinician which should include: logo, name, title, tel, email, web address and tagline
Nice to have
• A banner image to create a similar look to the website at www.healerathearth.ca
Should not have
• Too cluttered or busy - must be clean and professional

```html
<!DOCTYPE html>
<html lang="en">
<head>
<meta charset="utf-8">
<title>Healer at the Hearth – business card landscape designs</title>
<link href="https://fonts.googleapis.com/css2?family=Cabin:wght@400;500;600&family=EB+Garamond:ital@1&display=swap" rel="stylesheet">
<style>
  :root {
    --cream: #e9e5db;
    --cream-soft: #f1eee8;
    --navy: #33658f;
    --navy-text: #2d5b86;
    --crimson: #a21e24;
    --ink: #111111;
    --heading: #1a1a1a;
    --frame: #a8a8a8;
    --white: #ffffff;
    --sans: "Cabin", "Gill Sans", sans-serif;
    --serif: "EB Garamond", Georgia, serif;
  }
  * { box-sizing: border-box; margin: 0; padding: 0; }
  html, body { width: 1200px; height: 927px; overflow: hidden; background: var(--white); }
  .sheet { position: relative; width: 1200px; height: 927px; font-family: var(--sans); }
  .sheet-title {
    position: absolute; left: 33px; top: 28px;
    font-family: var(--sans); font-weight: 400; font-size: 26px; color: var(--heading);
  }
  .card {
    position: absolute; width: 383px; height: 218px;
    border: 1px solid var(--frame); overflow: hidden;
  }
  .col-front { left: 171px; }
  .col-back { left: 644px; }
  .row-1 { top: 129px; }
  .row-2 { top: 364px; }
  .row-3 { top: 601px; }

  /* Front */
  .front--cream { background: var(--cream); }
  .front--navy { background: var(--navy); }
  .front--crimson { background: var(--crimson); }
  .brand {
    position: absolute; left: 88px; top: 42px;
    display: flex; align-items: center; gap: 14px;
  }
  .brand-dot { width: 50px; height: 50px; border-radius: 50%; }
  .brand-name {
    font-family: var(--sans); font-weight: 400; font-size: 28px; line-height: 30px;
  }
  .front--cream .brand-dot { background: var(--crimson); }
  .front--cream .brand-name { color: var(--navy-text); }
  .front--navy .brand-dot, .front--crimson .brand-dot { background: var(--white); }
  .front--navy .brand-name, .front--crimson .brand-name { color: var(--white); }
  .tagline {
    position: absolute; left: 0; right: 0; bottom: 20px; text-align: center;
    font-family: var(--serif); font-style: italic; font-size: 18px;
  }
  .front--cream .tagline { color: var(--navy-text); }
  .front--navy .tagline, .front--crimson .tagline { color: var(--white); }

  /* Back */
  .back--plain { background: var(--white); }
  .back--navy { background: var(--navy); }
  .back--crimson { background: var(--crimson); }
  .back-shape { position: absolute; inset: 0; width: 100%; height: 100%; }
  .contact {
    position: absolute; right: 30px; top: 44px; text-align: right;
    color: var(--ink);
  }
  .back--crimson .contact { right: 60px; }
  .back--navy .contact { right: 26px; }
  .person-name { font-size: 24px; font-weight: 400; line-height: 26px; }
  .person-role { font-size: 12.5px; font-weight: 600; line-height: 14px; }
  .back--navy .person-name, .back--navy .person-role { color: var(--navy-text); }
  .back--crimson .person-name, .back--crimson .person-role { color: var(--crimson); }
  .contact-line { font-size: 16px; line-height: 22px; }
  .contact-lines { margin-top: 16px; }
  .contact-label { font-size: 10px; }
  .web { margin-top: 8px; font-size: 16px; font-weight: 600; }
</style>
</head>
<body>
<main class="sheet">
  <h1 class="sheet-title">Healer at the Hearth - business card landscape designs</h1>

  <!-- Fronts -->
  <section class="card col-front row-1 front--cream">
    <div class="brand"><span class="brand-dot"></span><span class="brand-name">Healer at<br>the Hearth</span></div>
    <p class="tagline">Patient Navigation &amp; Advocacy Services</p>
  </section>
  <section class="card col-front row-2 front--navy">
    <div class="brand"><span class="brand-dot"></span><span class="brand-name">Healer at<br>the Hearth</span></div>
    <p class="tagline">Patient Navigation &amp; Advocacy Services</p>
  </section>
  <section class="card col-front row-3 front--crimson">
    <div class="brand"><span class="brand-dot"></span><span class="brand-name">Healer at<br>the Hearth</span></div>
    <p class="tagline">Patient Navigation &amp; Advocacy Services</p>
  </section>

  <!-- Backs -->
  <section class="card col-back row-1 back--plain">
    <div class="contact">
      <p class="person-name">Martin Reeve</p>
      <p class="person-role">MD &amp; Co-Founder</p>
      <div class="contact-lines">
        <p class="contact-line"><span class="contact-label">Tel:</span> 647-555-0142</p>
        <p class="contact-line"><span class="contact-label">Email:</span> info@healerathearth.ca</p>
      </div>
      <p class="web">www.healerathearth.ca</p>
    </div>
  </section>

  <section class="card col-back row-2 back--navy">
    <svg class="back-shape" viewBox="0 0 383 218" preserveAspectRatio="none" aria-hidden="true">
      <defs>
        <linearGradient id="banner-tones" x1="0" y1="0" x2="1" y2="1">
          <stop offset="0" stop-color="#5d8fc4"/>
          <stop offset="0.55" stop-color="#b9d3ec"/>
          <stop offset="1" stop-color="#d9a88d"/>
        </linearGradient>
        <clipPath id="banner-clip"><rect x="0" y="0" width="140" height="218"/></clipPath>
      </defs>
      <rect x="0" y="0" width="140" height="218" fill="url(#banner-tones)" role="img" aria-label="Banner photo: a caregiver's hand resting on an older person's hand"/>
      <ellipse cx="232" cy="100" rx="160" ry="140" fill="var(--white)"/>
    </svg>
    <div class="contact">
      <p class="person-name">Martin Reeve</p>
      <p class="person-role">MD &amp; Co-Founder</p>
      <div class="contact-lines">
        <p class="contact-line"><span class="contact-label">Tel:</span> 647-555-0142</p>
        <p class="contact-line"><span class="contact-label">Email:</span> info@healerathearth.ca</p>
      </div>
      <p class="web">www.healerathearth.ca</p>
    </div>
  </section>

  <section class="card col-back row-3 back--crimson">
    <svg class="back-shape" viewBox="0 0 383 218" preserveAspectRatio="none" aria-hidden="true">
      <ellipse cx="200" cy="95" rx="172" ry="140" fill="var(--white)"/>
    </svg>
    <div class="contact">
      <p class="person-name">Martin Reeve</p>
      <p class="person-role">MD &amp; Co-Founder</p>
      <div class="contact-lines">
        <p class="contact-line"><span class="contact-label">Tel:</span> 647-555-0142</p>
        <p class="contact-line"><span class="contact-label">Email:</span> info@healerathearth.ca</p>
      </div>
      <p class="web">www.healerathearth.ca</p>
    </div>
  </section>
</main>
</body>
</html>
```